Vantorq, Business Intelligence Consultant Web Design

We need a web design for a Business Intelligence Consultant Enterprise.
We design, develop and mantain management systems and reports that delivered to the final user a complete information about their business. With that information they can take better management decisions.
Our principal service is KLV Business Intelligence proyects, using KLV Data Vault and KLV Report Suite tools.
Also we develop web systems that integrate mobile technology with KLV Systems and end user database systems.

Our principal objective is to be a partner of our clients more than a service provider, the idea is to offer a complete service to our customers that allow both companies grow togheter.

The final design must present our list of services and products, and show our experience in business intelligence projects.

Target Market(s)

Companies that runs KLV systems, Business companies, companies with production processes, retail, logistic process (inventory management)

Industry/Entity Type

Business

Requirements
Must have
• The brochure must have 4 pages:
Home
Empresa
Business Intelligence
Aplicaciones empresariales móviles
Metodología

And a contact form to receive customer contact.
- Name
- Company
- Contact Email
- Message text

For the color I will upload both company logos with different colors that u can use. Obviously you can add color if you want.
Nice to have
• The principal idea is to show to customer that all information of his business can be summarized on one graphic panel and can be consulted from any device.

Is nice to have business graphics on the web design, maybe abstract and give the idea of management information can be obtained easily.

Should not have
• Please, PLEASE!, don't use on the web site a meeting photo or people watching a business report on a lobby or some business man making a presentation.
Neither images of team building or people at the office.

That images are too used to present the business intelligence concept and the principal idea is to have information, and not people working hard to obtain that.

```html
<!DOCTYPE html>
<html lang="en">
<head>
<meta charset="utf-8">
<title>Vantorq – Business Intelligence</title>
<link rel="stylesheet" href="https://fonts.googleapis.com/css2?family=Arimo:wght@400;700&display=swap">
<style>
:root{
  --page:#f7f7f7;
  --frame:#dcdcdc;
  --ink:#222;
  --text:#333;
  --muted:#777;
  --nav:#333333;
  --brand:#e3262b;
  --brand-grey:#777;
  --link:#1a86b8;
  --rule:#cfcfcf;
  --navy:#23456f;
  --field:#f1f1f1;
}
*{box-sizing:border-box;margin:0;padding:0}
html,body{width:884px;height:1200px;overflow:hidden;background:#fff;font-family:"Arimo",Arial,sans-serif;color:var(--text)}
.canvas{position:relative;width:884px;height:1200px}
.page{position:absolute;left:88px;top:0;width:709px;height:1154px;background:var(--page);border:1px solid var(--frame);border-top:none}
.abs{position:absolute}
.logo{left:104px;top:30px;display:flex;align-items:center;gap:10px}
.logo-mark{width:32px;height:32px;border:6px solid var(--brand)}
.logo-name{font-size:36px;color:var(--brand-grey);font-weight:400;letter-spacing:.5px}
.follow{display:flex;align-items:center;gap:4px;font-size:9px;color:var(--ink)}
.follow span.txt{margin-right:3px}
.soc{width:12px;height:12px;border-radius:2px}
.search{left:615px;top:63px;width:166px;height:20px;background:#1e1e1e;border-radius:4px;color:#fff;font-size:10px;padding:4px 10px}
.search svg{position:absolute;right:6px;top:4px}
.nav{left:88px;top:102px;width:709px;height:38px;background:var(--nav);box-shadow:0 6px 6px -2px rgba(0,0,0,.45)}
.nav ul{list-style:none;display:flex;align-items:center;height:100%;padding-left:46px}
.nav li{color:#fff;font-size:10.5px;font-weight:700;padding:0 23px;border-right:1px solid #555;line-height:22px}
.nav li:last-child{border:none}
.nav li.active{padding:0;margin-right:23px;border:none}
.nav li.active span{background:#fff;color:var(--ink);border-radius:3px;padding:3px 8px}
.hero-art{left:184px;top:172px;width:250px;height:230px;border-radius:50%;background:radial-gradient(circle,#e9eef5 0%,#d8e2ef 40%,rgba(247,247,247,0) 70%)}
.hero-title{left:482px;top:207px;font-size:26px;font-weight:700;color:#111;line-height:25px}
.hero-lead{left:482px;top:271px;width:230px;font-size:10px;line-height:14.6px;color:var(--muted);letter-spacing:.3px}
.hero-note{left:482px;top:330px;width:230px;font-size:8.6px;line-height:14.6px;color:var(--muted)}
.arrow{width:30px;height:29px;background:#cfcfcf;border:1px solid #bbb}
.hero-bar{left:112px;top:417px;width:661px;height:8px;background:#333}
.globe{left:106px;top:452px;width:176px;height:116px;background:linear-gradient(135deg,#1d6fb8,#5fb4ea 55%,#cfeafb)}
h2{position:absolute;font-weight:400;color:#222}
.exp-title{left:298px;top:454px;font-size:17.6px}
.exp-copy{left:299px;top:481px;width:485px;font-size:8.8px;line-height:18.2px;color:#222}
.more{display:flex;align-items:center;gap:5px;font-size:8.4px;font-weight:700;color:var(--link)}
.more i{width:9px;height:9px;border-radius:50%;background:#444;position:relative}
.more i::after{content:"";position:absolute;left:2px;top:4px;width:5px;height:1px;background:#fff;box-shadow:0 0 0 0 #fff}
.more i::before{content:"";position:absolute;left:4px;top:2px;width:1px;height:5px;background:#fff}
.sec-title{font-size:17.5px}
.rule{height:1px;background:var(--rule)}
.svc{width:128px;font-size:8.8px;line-height:14.7px;color:#222}
.svc b{font-weight:700}
.thumb{width:76px;height:76px;background:#fff;border:1px solid #ddd;box-shadow:0 0 0 2px #eee}
.form-panel{left:541px;top:856px;width:232px;height:280px;background:#fff;border:1px solid #e2e2e2}
.form-tab{left:537px;top:868px;width:212px;height:23px;background:var(--navy);color:#fff;font-size:8.4px;padding:7px 14px;box-shadow:0 2px 3px rgba(0,0,0,.3)}
.label{font-size:8.4px;color:#444}
.label em{color:var(--brand);font-style:normal}
.field{width:186px;height:16px;background:var(--field);border:1px solid #e6e6e6;font-size:7.4px;color:#c4c4c4;padding:3px 7px}
.submit{left:563px;top:1103px;width:67px;height:20px;border-radius:5px;background:linear-gradient(#3b6597,#1f3f6a);color:#fff;font-size:9px;font-weight:700;text-align:center;line-height:20px;box-shadow:0 2px 3px rgba(0,0,0,.35)}
.photo{left:118px;top:960px;width:356px;height:144px;background:linear-gradient(90deg,#b88a5d 0%,#d9b38a 20%,#9aa8b6 35%,#c9d3dd 60%,#e6e9ec 100%)}
.foot{font-size:8px;color:#222}
</style>
</head>
<body>
<div class="canvas">
  <div class="page"></div>

  <header>
    <div class="abs logo"><div class="logo-mark"></div><div class="logo-name">Vantorq</div></div>
    <div class="abs follow" style="left:670px;top:37px"><span class="txt">Follow Us</span><i class="soc" style="background:#3b5998"></i><i class="soc" style="background:#2aa3d8"></i><i class="soc" style="background:#1a80b6"></i><i class="soc" style="background:#f28a1f"></i></div>
    <div class="abs search">Search
      <svg width="12" height="12" viewBox="0 0 12 12"><circle cx="5" cy="5" r="3.5" fill="none" stroke="#aaa" stroke-width="1.4"/><line x1="7.5" y1="7.5" x2="11" y2="11" stroke="#aaa" stroke-width="1.6"/></svg>
    </div>
    <nav class="abs nav"><ul>
      <li class="active"><span>Home</span></li>
      <li>Empresa</li>
      <li>Business Intelligence</li>
      <li>Aplicaciones empresariales móviles</li>
      <li>Metodología</li>
    </ul></nav>
  </header>

  <section class="hero">
    <div class="abs hero-art" role="img" aria-label="Illustration of a classroom presentation scene in blue and red"></div>
    <div class="abs arrow" style="left:88px;top:268px"><svg width="28" height="27" viewBox="0 0 28 27"><polyline points="17,6 10,13.5 17,21" fill="none" stroke="#fff" stroke-width="2.5"/></svg></div>
    <div class="abs arrow" style="left:766px;top:268px"><svg width="28" height="27" viewBox="0 0 28 27"><polyline points="11,6 18,13.5 11,21" fill="none" stroke="#fff" stroke-width="2.5"/></svg></div>
    <div class="abs hero-title">Management<br>Information</div>
    <p class="abs hero-lead">Lorem Ipsum available, but the majority have suffered alteration in some form, by injected humour, or randomised words.</p>
    <p class="abs hero-note">Lorem Ipsum, you need to be sure there isn't anything embarrassing hidden in the middle of text.</p>
    <div class="abs hero-bar"></div>
  </section>

  <section class="experience">
    <div class="abs globe" role="img" aria-label="Blue digital globe with network lines"></div>
    <h2 class="exp-title">Our experience in business intelligence projects.</h2>
    <p class="abs exp-copy">Lorem ipsum dolor sit amet, consectetur adipisicing elit, sed do eiusmod tempor incididunt ut labore et &nbsp;dolore magna aliqua. Ut enim ad minim veniam, quis nostrud exercitation ullamco laboris nisi ut aliquip ex commodo consequat. Duis aute irure dolor in reprehenderit in voluptate velit esse cillum dolore eu fugiat nulla pariatur. Excepteur sint occaecat cupidatat non proident, sunt in culpa qui officia deserunt mollit anim id est laborum.</p>
    <a class="abs more" style="left:714px;top:563px"><i></i>Read More</a>
  </section>

  <section class="services">
    <h2 class="sec-title" style="left:106px;top:591px">Our services</h2>
    <div class="abs rule" style="left:104px;top:628px;width:383px"></div>

    <svg class="abs" style="left:107px;top:648px" width="30" height="36" viewBox="0 0 30 36"><rect x="2" y="2" width="22" height="32" fill="#4fb3e0"/><rect x="2" y="2" width="5" height="32" fill="#2b7fb0"/><rect x="12" y="2" width="5" height="10" fill="#fff"/></svg>
    <p class="abs svc" style="left:150px;top:647px"><b>The point of using Lorem Ipsum</b> is that it has a more-or-less normal distribution of letters, as opposed to using 'Content here, content here', making it look like readable English.</p>
    <a class="abs more" style="left:209px;top:753px"><i></i>Read More</a>

    <svg class="abs" style="left:300px;top:646px" width="38" height="38" viewBox="0 0 38 38"><rect x="2" y="10" width="30" height="26" fill="#d9792a"/><rect x="7" y="15" width="20" height="18" fill="#e89447" stroke="#b5611c"/><polygon points="2,10 32,10 36,4 8,4" fill="#f1c34a"/></svg>
    <p class="abs svc" style="left:353px;top:647px"><b>Many desktop</b> publishing packages and web page editors now use Lorem Ipsum as their default model text, and a search for 'lorem ipsum' will uncover many web sites still in their infancy.</p>
    <a class="abs more" style="left:418px;top:753px"><i></i>Read More</a>

    <svg class="abs" style="left:104px;top:784px" width="30" height="36" viewBox="0 0 30 36"><rect x="2" y="3" width="26" height="31" fill="#d9a25a"/><rect x="5" y="6" width="20" height="26" fill="#fafafa"/><rect x="10" y="1" width="10" height="5" fill="#999"/><g stroke="#bbb"><line x1="8" y1="12" x2="22" y2="12"/><line x1="8" y1="17" x2="22" y2="17"/><line x1="8" y1="22" x2="22" y2="22"/><line x1="8" y1="27" x2="22" y2="27"/></g></svg>
    <p class="abs svc" style="left:150px;top:782px"><b>Various versions</b> have evolved over the years, sometimes by accident, sometimes on purpose (injected humour and the like).</p>
    <a class="abs more" style="left:209px;top:857px"><i></i>Read More</a>

    <svg class="abs" style="left:305px;top:784px" width="34" height="34" viewBox="0 0 34 34"><circle cx="17" cy="17" r="15" fill="#3a5fa8" stroke="#c9d4ea" stroke-width="2"/><text x="17" y="24" text-anchor="middle" font-family="Arimo,Arial,sans-serif" font-size="20" font-weight="700" fill="#fff">?</text></svg>
    <p class="abs svc" style="left:353px;top:782px"><b>Contrary to popular</b> belief, Lorem Ipsum is not simply random text. It has roots in a piece of classical Latin literature from 45 BC.</p>
    <a class="abs more" style="left:417px;top:857px"><i></i>Read More</a>
  </section>

  <section class="products">
    <h2 class="sec-title" style="left:539px;top:595px">Our Products</h2>
    <div class="abs rule" style="left:533px;top:628px;width:240px"></div>
    <div class="abs thumb" style="left:533px;top:648px"><svg width="74" height="74" viewBox="0 0 74 74"><rect x="4" y="6" width="66" height="8" fill="#f1b72f"/><circle cx="24" cy="46" r="18" fill="#dfe9f5" stroke="#2b5a9b" stroke-width="2"/><rect x="50" y="24" width="18" height="44" fill="#e8eef7"/><rect x="14" y="38" width="10" height="4" fill="#2b5a9b"/><rect x="14" y="44" width="16" height="4" fill="#2b5a9b"/></svg></div>
    <div class="abs thumb" style="left:614px;top:648px"><svg width="74" height="74" viewBox="0 0 74 74"><g fill="#4a78b8"><rect x="20" y="26" width="3" height="8"/><rect x="26" y="22" width="3" height="12"/><rect x="32" y="18" width="3" height="16"/><rect x="38" y="24" width="3" height="10"/><rect x="44" y="14" width="3" height="20"/></g><line x1="14" y1="34" x2="60" y2="34" stroke="#999"/><g fill="none" stroke="#c33" stroke-width="2"><circle cx="20" cy="58" r="7"/><circle cx="37" cy="58" r="7"/><circle cx="54" cy="58" r="7"/></g></svg></div>
    <div class="abs thumb" style="left:696px;top:648px"><svg width="74" height="74" viewBox="0 0 74 74"><rect x="4" y="6" width="66" height="6" fill="#f1b72f"/><ellipse cx="42" cy="38" rx="20" ry="12" fill="#d8e0ea"/><g fill="#c0392b"><rect x="38" y="28" width="4" height="14"/><rect x="48" y="26" width="4" height="16"/></g><g fill="#f1b72f"><rect x="32" y="56" width="20" height="3"/><rect x="32" y="61" width="14" height="3"/></g><rect x="32" y="66" width="24" height="3" fill="#2b5a9b"/></svg></div>
    <div class="abs thumb" style="left:533px;top:730px"><svg width="74" height="74" viewBox="0 0 74 74"><rect x="4" y="4" width="66" height="5" fill="#2b5a9b"/><circle cx="46" cy="42" r="22" fill="#2b4d7a"/><circle cx="46" cy="42" r="16" fill="#dbe4ef"/><path d="M32 38 A16 16 0 0 1 58 32" fill="none" stroke="#e67e22" stroke-width="4"/><line x1="46" y1="42" x2="52" y2="30" stroke="#c0392b" stroke-width="2"/><rect x="6" y="46" width="4" height="14" fill="#2b5a9b"/><rect x="11" y="52" width="4" height="8" fill="#c0392b"/></svg></div>
    <div class="abs thumb" style="left:614px;top:730px"><svg width="74" height="74" viewBox="0 0 74 74"><rect x="4" y="4" width="66" height="5" fill="#f1b72f"/><rect x="30" y="12" width="20" height="50" fill="#e8eef7"/><g fill="#2b5a9b"><rect x="54" y="40" width="3" height="30"/><rect x="59" y="48" width="3" height="22"/><rect x="64" y="30" width="3" height="40"/></g><path d="M14 66 A12 12 0 0 1 38 66" fill="none" stroke="#2ecc71" stroke-width="4"/></svg></div>
    <div class="abs thumb" style="left:696px;top:730px"><svg width="74" height="74" viewBox="0 0 74 74"><line x1="12" y1="10" x2="12" y2="56" stroke="#999"/><line x1="12" y1="56" x2="70" y2="56" stroke="#999"/><rect x="22" y="28" width="8" height="28" fill="#2b5a9b"/><rect x="34" y="38" width="8" height="18" fill="#4a78b8"/><rect x="48" y="14" width="8" height="42" fill="#2ea44f"/><rect x="60" y="14" width="5" height="42" fill="#2ea44f"/><rect x="10" y="62" width="58" height="6" fill="#e8eef7"/></svg></div>
    <a class="abs more" style="left:690px;top:821px"><i></i>view all products</a>
  </section>

  <section class="integration">
    <h2 class="sec-title" style="left:106px;top:906px">Intergration with KLV &amp; End User Database</h2>
    <div class="abs rule" style="left:104px;top:942px;width:383px"></div>
    <div class="abs photo" role="img" aria-label="Photo of a workstation with two monitors showing business software"></div>
    <a class="abs more" style="left:410px;top:1126px"><i></i>Learn More</a>
  </section>

  <section class="contact">
    <div class="abs form-panel"></div>
    <div class="abs form-tab">Fill in your details and we'll get back to you...</div>
    <div class="abs label" style="left:563px;top:901px">Name<em>*</em></div>
    <div class="abs field" style="left:563px;top:914px">Full name</div>
    <div class="abs label" style="left:563px;top:940px">Company</div>
    <div class="abs field" style="left:563px;top:952px">Company name</div>
    <div class="abs label" style="left:563px;top:978px">Email<em>*</em></div>
    <div class="abs field" style="left:563px;top:990px">Email address</div>
    <div class="abs label" style="left:563px;top:1016px">Message<em>*</em></div>
    <div class="abs field" style="left:563px;top:1029px;height:63px"></div>
    <div class="abs submit">Submit</div>
  </section>

  <footer>
    <div class="abs foot" style="left:90px;top:1173px">© 2012, Vantorq , All Rights Reserved</div>
    <div class="abs follow" style="left:684px;top:1171px"><span class="txt">Follow Us</span><i class="soc" style="background:#3b5998"></i><i class="soc" style="background:#2aa3d8"></i><i class="soc" style="background:#1a80b6"></i><i class="soc" style="background:#f28a1f"></i></div>
  </footer>
</div>
</body>
</html>
```